Tavington Inc 1 pg brochure for entrepreneurs

We need a one page brochure (2 sided) designed for a finance and strategy consulting company called Tavington Inc. which does work in Canada and the United States currently. This company works with entrepreneurs, helping them to establish finance operations, evaluate their financial infomation and apply insight from it to business strategies. Essentially we help entrepreneurs grow their business ... we take care of their finance needs and give them sound business advice ... allowing them to focus on their core business and business strategy.

This one page brochure is meant to caputure what services we provide but also positon that we are also entrepreneurs and we understand how entrepreneurs think .... we not only bring technical competence but cultural insight in this regard as well. We understand how nimble and stealth an entrepreneur's business is so we don't gouge them with expensive consulting fees. We don't want to look like a massive corporation ...we want to look professional, smart and reliable. We want to reflect that we are entrepreneural ourselves even in fact that we have a niche offering that is totally targeted to businesses of this nature.

Major emphasis points for the piece are
1) our core values, this could be a side bar or box
2) the credentials of our founder, he is technically competent and an entrepreneur himself (we have his picture to include)
3) our offerings, what we can do for a company, the client quotes provided are a good illustration of what we offer, the relief we provide a client and of what value we provide - make sure you read these, this could also be a side bar or box, some kind of special call out so the service offerings are very clear

The brochure needs to be editable, so in a format that we can work with it for future, if we need to make updates, one that we can use in Microsoft word and convert to a PDF format. It will be emailed to people (in pdf) and also brought to meetings.

We have a new logo and this design should be an extenstion of it from a colour, look and feel perspective. The piece should also be clean and not too copy heavy so we encourage use of sub-heads, whitespace, etc.

When we send this piece out or hand it to someone, the impression should be "I am comfortable with Tavington Inc. they can help me and are people who get me, people I can trust to work closely with me on my business who are personally vested in my success".
Updates

Hello all, thank you for sumitting designs, there is some great work here.  A few changes/requests ...

Pls add the following headline on the front page right off the top

Entrepreneurs helping entrepreneurs, providing strategic financial services

Can we put Services on the front page? and call them out with treatment in a text box or with something strong that creates emphasis

Can the quote pls be broken up as opposed to one long list of 6 quotes? They can be floated throughout the piece, we can use less of them (or not) and put them on the front and back of the brochure? 

Also looking for the final product to be a little more bold in colour ...

Thx all, let us know if you have questions

Target Market(s)

Individuals (CEO) who runs their own established, yet growing business, who needs a business-minded CFO

Industry/Entity Type

Financial

Requirements
Must have
• Must have photo of founder, include his name and credentials under photo
All copy provide must be included
If not sure of a headline put in dummy text and we will provide headline or sub head copy
Should not have
• Fonts to be clean, no serif fonts. Should compliment logo, not the same font exactly but easily replicable in Microsoft Word and complimentary
No illustrations or cliche clip art

```html
<!DOCTYPE html>
<html lang="en">
<head>
<meta charset="utf-8">
<title>Tavington Inc – Brochure</title>
<link href="https://fonts.googleapis.com/css2?family=Saira+Semi+Condensed:wght@300;400;600&display=swap" rel="stylesheet">
<style>
:root{
  --bg:#5c5c5e;
  --teal:#4fb0cc;
  --blue:#1d5fae;
  --navy:#2b4192;
  --slate:#5a5b7e;
  --taupe:#6b6466;
  --white:#ffffff;
  --quote:#1f4e9c;
}
*{margin:0;padding:0;box-sizing:border-box}
html,body{width:1200px;height:1000px;overflow:hidden}
body{background:var(--bg);font-family:"Saira Semi Condensed",sans-serif;position:relative}
.page{position:absolute;top:96px;width:570px;height:808px;box-shadow:0 2px 8px rgba(0,0,0,.45);overflow:hidden}
.page--front{left:22px}
.page--back{left:613px}
.block{position:absolute}
.heading{position:absolute;color:var(--white);font-size:18px;font-weight:400;letter-spacing:.4px}
.copy{position:absolute;font-size:10.6px;line-height:11.6px;text-align:justify;color:var(--white);hyphens:auto;-webkit-hyphens:auto}
.copy p{text-indent:34px}
.copy b{font-weight:600}

/* front */
.brand{background:var(--white);left:0;top:0;width:324px;height:134px}
.brand__mark{position:absolute;left:40px;top:33px;width:75px;height:72px;border:4px solid var(--blue)}
.brand__name{position:absolute;left:124px;top:44px;font-size:30px;font-weight:400;color:var(--slate)}
.front-top-accent{background:var(--teal);left:324px;top:0;width:246px;height:134px}
.front-top-square{background:var(--taupe);left:514px;top:0;width:56px;height:57px}
.mission{background:var(--blue);left:0;top:134px;width:570px;height:107px}
.who{background:var(--slate);left:0;top:241px;width:570px;height:153px}
.founder-photo{left:26px;top:242px;width:125px;height:152px;background:linear-gradient(180deg,#3a3a3c,#1c1c20)}
.quotes-panel{background:var(--teal);left:0;top:394px;width:324px;height:414px}
.bio-panel{background:var(--taupe);left:324px;top:394px;width:246px;height:414px}
.front-foot-square{background:var(--taupe);left:0;top:781px;width:28px;height:27px}
.quotes{color:var(--quote)}
.quotes p + p{margin-top:12px}
.quotes .quotes__first{margin-top:22px}

/* back */
.values{background:var(--teal);left:0;top:0;width:570px;height:324px}
.values-square{background:var(--blue);left:0;top:0;width:28px;height:28px}
.values-copy{font-size:12px;line-height:13.6px}
.values-copy p + p{margin-top:14px}
.services{background:var(--navy);left:0;top:324px;width:324px;height:484px}
.services-square{background:var(--blue);left:267px;top:324px;width:57px;height:57px}
.contact{background:var(--slate);left:324px;top:324px;width:246px;height:427px}
.contact-square{background:var(--teal);left:542px;top:724px;width:28px;height:27px}
.footer-brand{background:var(--white);left:324px;top:751px;width:246px;height:57px}
.footer-brand__mark{position:absolute;left:67px;top:12px;width:32px;height:32px;border:2px solid var(--blue)}
.footer-brand__name{position:absolute;left:105px;top:17px;font-size:15px;color:var(--slate)}
.service-list{position:absolute;left:22px;top:420px;width:277px;list-style:none;color:var(--white);font-size:12.4px;line-height:13.8px;text-align:justify}
.service-list li{position:relative;padding-left:38px}
.service-list li::before{content:"·";position:absolute;left:0;top:0}
.service-list li + li{margin-top:14px}
.contact-info{position:absolute;left:353px;top:425px;color:var(--white);font-size:12.4px;line-height:13.8px;white-space:nowrap}
</style>
</head>
<body>

<section class="page page--front">
  <div class="block brand">
    <span class="brand__mark"></span>
    <span class="brand__name">Tavington Inc</span>
  </div>
  <div class="block front-top-accent"></div>
  <div class="block front-top-square"></div>

  <div class="block mission"></div>
  <h2 class="heading" style="left:61px;top:141px">MISSION</h2>
  <div class="copy" style="left:28px;top:169px;width:484px;text-align:left">
    <p>Tavington Inc. provides strategic financial services to entrepreneurs.</p>
    <div>We are entrepreneurs assisting entrepreneurs. By engaging us, entrepreneurs can regularly access senior executive financial acumen and strategic discipline without having to hire a full-time financial executive or overspend on third-party service providers who are transactional in nature.</div>
  </div>

  <div class="block who"></div>
  <div class="block founder-photo" role="img" aria-label="Portrait photo of the founder, Adrian Kessler"></div>
  <h2 class="heading" style="left:228px;top:258px">WHO ARE WE?</h2>
  <div class="copy" style="left:196px;top:286px;width:325px;text-align:left">
    <p>Tavington Inc. evolved out of the companies, partnerships and relationships that Adrian Kessler, its founder, has nurtured and built over the last 22 years. Mr. Kessler, the founder of Tavington, is an entrepreneur himself having built his own companies and managed several successful investment funds whose mandates were to invest in entrepreneurial growth companies.</p>
  </div>

  <div class="block quotes-panel"></div>
  <div class="copy quotes" style="left:26px;top:430px;width:273px">
    <p>Over his career, he has worked extensively with entrepreneurs like himself who have struggled to build an experienced and engaged executive management team. Common comments from visionary entrepreneurs (which Tavington Inc. helps address) include:</p>
    <p class="quotes__first">“I need a financial executive to integrate my operating objectives with my financial ones. They are not aligned and are working against each other”</p>
    <p>“If I could hire a right-hand who I trust intimately to help me with financial matters, I could free up more time to run the business or work on strategy”</p>
    <p>“I need a financial executive who gets the numbers, can think strategically and translate that combined expertise and understanding into forward-looking corporate strategies”</p>
    <p>“I need a financial executive who understands the inherent makeup of an entrepreneur”</p>
    <p>“I would be a billionaire if I could implement better financial systems and apply strategic discipline.”</p>
    <p>“If I could hire my equal in a financial capacity, my executive team would be complete”</p>
  </div>

  <div class="block bio-panel"></div>
  <div class="copy" style="left:354px;top:407px;width:188px">
    <div>Mr. Kessler has a proven track record of developing and implementing strategic corporate policy. His experience and education is in corporate finance, portfolio management and building businesses. He is a registered Portfolio Manager. He also has earned an MBA from the Northfield University (1995) and is a Chartered Financial Analyst (CFA, 1999). He applies this competence to evaluating an entrepreneur’s vision and corporate strategies and assisting in translating them into higher growth, improved efficiency and higher profitability. He has extensive experience in public and private, debt and equity capital markets, involving raising, managing and investing capital and completing corporate transactions. He has evaluated hundreds of corporate business strategies for potential investment. Other core skills include financial and tax analysis, working with high-performing investment teams, managing financial and accounting functions, designing and implementing operational and compliance systems.</div>
  </div>
  <div class="block front-foot-square"></div>
</section>

<section class="page page--back">
  <div class="block values"></div>
  <div class="block values-square"></div>
  <h2 class="heading" style="left:79px;top:26px">CORE VALUES</h2>
  <div class="copy values-copy" style="left:48px;top:68px;width:462px">
    <p>We love working with entrepreneurs because they like <b>adventure</b>. We understand the high energy, creativity and passion required to take high risks and achieve a corporate vision.</p>
    <p>We like entrepreneurs because they are focused on <b>achievement.</b> They are “can-do” people who take action.</p>
    <p>We like entrepreneurs because their business relationships are like <b>family</b>. Entrepreneurs are personally invested and value personal relationships with amazing people.</p>
    <p>We like entrepreneurs because they work hard and live well. <b>Health and wellness</b> is as important as financial success, and most of all having fun is central to the mind set of most successful entrepreneurs.</p>
  </div>

  <div class="block services"></div>
  <div class="block services-square"></div>
  <h2 class="heading" style="left:58px;top:372px">SERVICES</h2>
  <ul class="service-list">
    <li>We work intimately with our clients to determine their corporate and personal objectives</li>
    <li>We evaluate corporate strategies and assist in aligning them with financial ones</li>
    <li>We assist in budgeting, investing, financial forecasting and analysis and asset management</li>
    <li>We develop and implement accountability financial systems, processes and reporting</li>
    <li>We manage capital raising efforts, tax structuring issues and corporate transactions including mergers, acquisitions, and the sale of your business;</li>
  </ul>

  <div class="block contact"></div>
  <div class="contact-info">
    Tavington Inc. 1180 Harlow St SW,<br>Calgary Alberta, Canada, T3K 4M1<br>416.555.0142<br><br>adriank@tavingtoninc.ca
  </div>
  <div class="block contact-square"></div>
  <div class="block footer-brand">
    <span class="footer-brand__mark"></span>
    <span class="footer-brand__name">Tavington Inc</span>
  </div>
</section>

</body>
</html>
```